Business Card Design and a letter head logo

50/50 share milker dairy farmer of 400 cows with a silage and haymaking sideline business
15 years farming currently looking for new opportunities within the dairy farming sector. trying to put together a portfolio to get another 50/50 share milking job aswell

Industry/Entity Type

Farming

Contact Information for Business Card

Birch Farming LTD
Corwin & Felicity Hartley
382 Kelvale Ridge Highway
RD1 Tawhiro 0184
Whangarei
hartley.corwin@lumenmail.co.nz
0273948261
(09) 4715293

```html
<!DOCTYPE html>
<html lang="en">
<head>
<meta charset="utf-8">
<title>Birch Farming LTD – Business Card</title>
<link href="https://fonts.googleapis.com/css2?family=Saira+Condensed:wght@300;400;600&display=swap" rel="stylesheet">
<style>
  :root {
    --backdrop: #e6e6e2;
    --card-light: #d3d8d0;
    --card-dark: #b9c0b6;
    --ink: #1c1d1b;
    --ink-soft: #2c2e2b;
    --art-dark: #141514;
    --art-mid: #3a3d39;
  }
  * { margin: 0; padding: 0; box-sizing: border-box; }
  html, body {
    width: 1200px;
    height: 892px;
    overflow: hidden;
    background: var(--backdrop);
  }
  .canvas {
    position: relative;
    width: 1200px;
    height: 892px;
  }
  .business-card {
    position: absolute;
    left: 100px;
    top: 160px;
    width: 1000px;
    height: 572px;
    background: linear-gradient(135deg, var(--card-light) 0%, var(--card-dark) 100%);
    box-shadow: 0 6px 24px rgba(0,0,0,0.18);
    font-family: "Saira Condensed", "Arial Narrow", sans-serif;
    color: var(--ink);
  }
  .cow-illustration {
    position: absolute;
    left: 40px;
    top: 150px;
    width: 370px;
    height: 390px;
    border-radius: 46% 40% 30% 36%;
    background: radial-gradient(ellipse at 45% 40%, var(--art-mid) 0%, var(--art-dark) 75%);
    opacity: 0.85;
  }
  .company-name {
    position: absolute;
    left: 430px;
    top: 34px;
    font-size: 66px;
    font-weight: 600;
    letter-spacing: 1px;
    line-height: 1;
  }
  .owner-names {
    position: absolute;
    right: 90px;
    top: 132px;
    font-size: 46px;
    font-weight: 300;
    line-height: 1;
    color: var(--ink-soft);
  }
  .owner-role {
    position: absolute;
    right: 60px;
    top: 196px;
    font-size: 18px;
    font-weight: 400;
    color: var(--ink-soft);
  }
  .contact-details {
    position: absolute;
    right: 40px;
    top: 300px;
    text-align: right;
    font-size: 25px;
    font-weight: 300;
    line-height: 1.25;
    list-style: none;
    color: var(--ink-soft);
  }
  .contact-details .gap { margin-top: 22px; }
</style>
</head>
<body>
<main class="canvas">
  <section class="business-card">
    <div class="cow-illustration" role="img" aria-label="Black stencil-style illustration of a dairy cow"></div>
    <h1 class="company-name">Birch Farming LTD</h1>
    <p class="owner-names">Corwin &amp; Felicity Hartley</p>
    <p class="owner-role">owner</p>
    <ul class="contact-details">
      <li>0273948261</li>
      <li>(09) 4715293</li>
      <li>hartley.corwin@lumenmail.co.nz</li>
      <li class="gap">382 Kelvale Ridge Highway RD1</li>
      <li>Tawhiro 0184 Whangarei</li>
    </ul>
  </section>
</main>
</body>
</html>
```